Lotus Bowl take out menu

We need a take out menu design using our menu attached. Info to include would be our address: 5817 Meridel Harrow Pkwy #204, Bayou Tresse, LA 70591. Phone number is 337-614-2953. website is www.lotusbowlvtr.example.

Industry/Entity Type

Asian Restaurant

```html
<!DOCTYPE html>
<html lang="en">
<head>
<meta charset="utf-8">
<title>Lotus Bowl Take-Out Menu</title>
<link href="https://fonts.googleapis.com/css2?family=Crimson+Text:ital,wght@0,400;0,600;0,700;1,700&display=swap" rel="stylesheet">
<style>
:root{
  --backdrop:#8e1a1d;
  --red:#a3161a;
  --red-deep:#7e1014;
  --paper:#ededed;
  --paper-alt:#e4e4e4;
  --cream:#f6f1e7;
  --ink:#262626;
  --muted:#7a7a7a;
  --band:#1d1d1d;
}
*{margin:0;padding:0;box-sizing:border-box}
html,body{width:1200px;height:1200px;overflow:hidden}
body{background:var(--backdrop);font-family:"Crimson Text",Georgia,serif;color:var(--ink);position:relative}
.sheet{position:absolute;left:235px;width:730px;height:566px;background:var(--paper);box-shadow:0 4px 14px rgba(0,0,0,.35)}
.sheet--outside{top:22px}
.sheet--inside{top:612px;display:flex}
.frame{border:1px dashed var(--red);position:absolute}

/* lunch */
.lunch{position:absolute;left:0;top:0;width:364px;height:566px;background:linear-gradient(90deg,var(--paper) 50%,var(--paper-alt) 50%)}
.lunch .frame{inset:12px}
.lunch h2{position:absolute;top:42px;width:100%;text-align:center;font-weight:400;font-size:12px;letter-spacing:.5px}
.lunch .note{position:absolute;top:64px;width:100%;text-align:center;font-size:6px}
.lunch .cols{position:absolute;top:103px;left:32px;right:32px;display:flex;gap:28px}
.col{flex:1;display:flex;flex-direction:column;gap:24px}
.lunch .col{gap:0}
.lunch .col .item{height:37px}

.item .row{display:flex;align-items:baseline;font-size:7.4px;line-height:1}
.item .leader{flex:1;border-bottom:1px dotted #555;margin:0 2px;transform:translateY(-1px)}
.item p{font-size:4.4px;color:var(--muted);line-height:1.15;margin-top:2px;max-width:95%}

/* story */
.red-field{position:absolute;left:364px;top:0;width:366px;height:566px;background:var(--red)}
.card{position:absolute;top:14px;height:537px;width:158px;background:var(--cream);border-radius:7px}
.card--story{left:12px;padding:58px 12px 0}
.card--story h3{position:absolute;top:58px;left:0;width:100%;text-align:center;color:var(--red);font-weight:400;font-size:11px}
.card--story .body{margin-top:31px;font-size:7.2px;line-height:1.55;text-align:justify}
.card--story .body p+p{margin-top:9px}
.brand{color:var(--red-deep);font-weight:700;display:flex;align-items:center;gap:4px;white-space:nowrap}
.brand i{display:block;border-radius:50%;background:var(--red)}
.card--story .brand{position:absolute;bottom:14px;left:0;width:100%;justify-content:center;font-size:16px}
.card--story .brand i{width:10px;height:10px}

/* cover */
.card--cover{left:193px}
.card--cover .frame{inset:11px}
.cover-name{position:absolute;top:114px;left:0;width:100%;text-align:center;font-size:23px;color:var(--red-deep);font-weight:700}
.cover-dot{position:absolute;top:62px;left:64px;width:30px;height:30px;border-radius:50%;background:var(--red)}
.takeout{position:absolute;top:256px;left:0;width:100%;text-align:center;color:var(--red-deep);font-style:italic;font-weight:700;line-height:.85}
.takeout span{display:block;font-size:21px}
.takeout strong{display:block;font-size:40px}
.phone{position:absolute;top:436px;width:100%;text-align:center;color:var(--red-deep);font-weight:700;font-size:17px}
.web{position:absolute;top:470px;width:100%;text-align:center;font-size:8.6px}
.addr{position:absolute;top:496px;width:100%;text-align:center;font-size:5.4px;line-height:1.3;color:var(--red-deep)}

/* inside panels */
.panel{position:relative;width:182.5px;height:566px}
.panel:nth-child(even){background:var(--paper-alt)}
.panel .frame{left:12px;right:12px;top:16px;bottom:16px}
.panel h2{font-weight:400;font-size:11.5px;text-align:center;letter-spacing:.4px}
.panel .frame h2{margin-top:32px}
.list{position:absolute;left:10px;right:10px;display:flex;flex-direction:column}
.band{display:block;margin:0 auto;width:112px;background:var(--band);color:#fff;font-size:5.4px;text-align:center;letter-spacing:.6px;padding:1.5px 0;border-radius:4px}
.panel--apps .brand{position:absolute;top:40px;left:14px;font-size:20px}
.panel--apps .brand i{width:13px;height:13px}
.panel--apps .frame{top:82px}
.sub{font-weight:400;font-size:11.5px;text-align:center;margin:12px 0 8px}
</style>
</head>
<body>

<section class="sheet sheet--outside">
  <div class="lunch">
    <div class="frame"></div>
    <h2>LUNCH MENU</h2>
    <div class="note">available Monday-Friday from 11am to 3pm</div>
    <div class="cols">
      <div class="col">
        <div class="item"><div class="row">Kung Pao Chicken<span class="leader"></span>$10</div><p>Chicken sautéed with roasted peanuts and dry red chili in Kung Pao sauce</p></div>
        <div class="item"><div class="row">Orange Chicken<span class="leader"></span>$10</div><p>Battered-fried chicken breast with dried chili peppers and stir fried in a tangy orange flavored sauce</p></div>
        <div class="item"><div class="row">Crispy Spicy Chicken<span class="leader"></span>$11</div><p>Crispy-diced chicken with Sichuan peppers, garlic, scallions and red and green bell peppers</p></div>
        <div class="item"><div class="row">General Tso's Chicken<span class="leader"></span>$10</div><p>Battered-fried chicken breast, stir fried in a sweet &amp; tangy chili sauce with chili peppers</p></div>
        <div class="item"><div class="row">Shredded Chicken in Spicy Garlic Sauce<span class="leader"></span>$11</div><p>Tender shredded chicken, wood ear mushrooms, bamboo shoots, broccoli, green and red bell peppers and water chestnuts</p></div>
        <div class="item"><div class="row">Sweet &amp; Sour Chicken<span class="leader"></span>$10</div><p>Crispy chicken with green bell peppers, onions and pineapple glazed in a homemade sweet and sour marinade</p></div>
        <div class="item"><div class="row">Oyster Beef<span class="leader"></span>$11</div><p>Tender cuts of steak wok fried with onions and marinated in a homemade oyster sauce</p></div>
        <div class="item"><div class="row">Black Pepper Steak<span class="leader"></span>$12</div><p>Tender cuts of steak mixed with onions and red and green bell peppers</p></div>
        <div class="item"><div class="row">Dancing Pork Belly<span class="leader"></span>$12</div><p>Braised Pork Belly on sizzling rice cracker</p></div>
        <div class="item"><div class="row">Twice Cooked Pork<span class="leader"></span>$11</div><p>Stir fried Pork Belly slices with leek and fermented black beans</p></div>
      </div>
      <div class="col">
        <div class="item"><div class="row">Lemon Peel Shrimp<span class="leader"></span>$12</div><p>Shrimp with fresh lemons in a sweet lemon sauce on a bed of shredded lettuce</p></div>
        <div class="item"><div class="row">Rice Wine Fish<span class="leader"></span>$11</div><p>White fish filet with rice wine mixed with onions, peas and carrots</p></div>
        <div class="item"><div class="row">Lotus Bowl Fried Rice<span class="leader"></span>$10</div><p>Shrimp, chicken, and beef, farm fresh eggs, onions, and scallions</p></div>
        <div class="item"><div class="row">Vegetarian White Fried Rice<span class="leader"></span>$9</div><p>Mixed vegetables with white rice</p></div>
        <div class="item"><div class="row">Lotus Bowl Lo Mein<span class="leader"></span>$10</div><p>Shrimp, chicken, and beef, farm fresh eggs, onions, and scallions</p></div>
        <div class="item"><div class="row">Vegetarian Lo Mein<span class="leader"></span>$9</div><p>Mixed vegetables with lo mein noodles</p></div>
        <div class="item"><div class="row">Mapo Tofu<span class="leader"></span>$9</div><p>Soft Tofu, scallion, Sichuan peppercorn and peppers</p></div>
        <div class="item"><div class="row">Spicy Garlic Eggplant<span class="leader"></span>$10</div><p>Chinese eggplant in spicy garlic sauce garnished with scallions</p></div>
        <div class="item"><div class="row">Stir Fried Eggplant<span class="leader"></span>$10</div><p>Chinese eggplant with sautéed green beans</p></div>
        <div class="item"><div class="row">Shiitake Baby Bok Choy<span class="leader"></span>$10</div><p>Sautéed baby bok-choy with Shiitake mushrooms in brown sauce</p></div>
      </div>
    </div>
  </div>

  <div class="red-field">
    <article class="card card--story">
      <h3>OUR STORY</h3>
      <div class="body">
        <p>At Lotus Bowl, we pride ourselves in serving fresh, authentic Sichuan Chinese cuisine delicately prepared by our expertly trained Chefs.</p>
        <p>Sichuan cuisine originates from southwest China between the Sichuan Basin and Tibetan Plateau. It is known for being both very spicy and flavorful, much like our own southern Louisiana cuisine.</p>
        <p>Our Executive Chef, Wen Liu grew up in the southwestern Chinese province of Sichuan, China where he began his training at fifteen years old under his grandfather's mentorship. Chef Liu became an acclaimed chef in his province, opening several restaurants and traveling throughout China to cater for many of China's elite. His dream was to share his Sichuan style with the world which lead him to the United States. He has worked in restaurants in both Houston and New York and we now welcome him to his new home in Bayou Tresse, Louisiana.</p>
        <p>We are very excited to bring to Bayou Tresse the authenticity of Chinese cuisine and hope you enjoy your experience dining with us.</p>
      </div>
      <div class="brand"><i></i>Lotus Bowl</div>
    </article>

    <article class="card card--cover">
      <div class="frame"></div>
      <div class="cover-dot"></div>
      <div class="cover-name">Lotus Bowl</div>
      <div class="takeout"><span>TAKE-OUT</span><strong>MENU</strong></div>
      <div class="phone">337-614-2953</div>
      <div class="web">www.lotusbowlvtr.example</div>
      <div class="addr">5817 Meridel Harrow Pkwy #204,<br>Bayou Tresse, LA 70591</div>
    </article>
  </div>
</section>

<section class="sheet sheet--inside">
  <div class="panel panel--apps">
    <div class="brand"><i></i>Lotus Bowl</div>
    <div class="frame">
      <h2>APPETIZERS</h2>
      <div class="list" style="top:68px;gap:6.5px">
        <div class="item"><div class="row">Edamame<span class="leader"></span>$4</div><p>Seasoned &amp; boiled soy bean</p></div>
        <div class="item"><div class="row">Scallion Pancakes<span class="leader"></span>$6</div><p>Traditional Chinese flatbread folded with oil and minced scallions and pan fried</p></div>
        <div class="item"><div class="row">Lotus Bowl Lettuce Wraps<span class="leader"></span>$8</div><p>Seasoned ground chicken drizzled with our secret sauce served with lettuce wraps</p></div>
        <div class="item"><div class="row">Salt &amp; Pepper Calamari<span class="leader"></span>$9</div><p>Crispy Calamari with green &amp; red peppers and onions</p></div>
        <div class="item"><div class="row">Buddha Bang Shrimp<span class="leader"></span>$9</div><p>Crispy fried shrimp tossed in our creamy spicy sauce</p></div>
        <div class="item"><div class="row">Drunken Chicken<span class="leader"></span>$8</div><p>Chicken, Thai chili in a house made spicy sauce</p></div>
        <div class="item"><div class="row">Sichuan Spiced Beef<span class="leader"></span>$9</div><p>Beef shank, beef tripe, cilantro, peanuts and celery</p></div>
        <div class="item"><div class="row">Beef Crispy Bottom Bao<span class="leader"></span>$10</div><p>Pan fried crispy bottom bao, stuffed with beef, drizzled with scallion oil sesame</p></div>
        <div class="item"><div class="row">Crispy Mala Beef Jerky<span class="leader"></span>$9</div><p>Dry fried shredded beef with various peppers in sesame oil</p></div>
        <div class="item"><div class="row">Fried Chicken Dumplings (6)<span class="leader"></span>$6</div><p>Chinese dumplings stuffed with chicken, shiitake mushrooms and bamboo shoots</p></div>
        <div class="item"><div class="row">Red Oil Dumplings (6)<span class="leader"></span>$7</div><p>Chicken filled dumplings in Sichuan red oil sauce with sesame</p></div>
        <div class="item"><div class="row">Pork Egg Rolls (2)<span class="leader"></span>$4</div><p>Hand rolled with julienned veggies with our sweet n' sour mustard sauce</p></div>
        <div class="item"><div class="row">Vegetarian Spring Rolls (3)<span class="leader"></span>$4</div><p>Traditional Asian roll served with a sweet chili sauce</p></div>
        <div class="item"><div class="row">Garlic Cucumber Salad<span class="leader"></span>$7</div><p>Sliced cucumber with a garlic vinaigrette</p></div>
        <div class="item"><div class="row">Hot n' Sour Soup<span class="leader"></span>$4</div><p>Tangy broth with bamboo shoot, wood ear mushrooms, tofu, egg and carrots</p></div>
        <div class="item"><div class="row">West Lake Soup<span class="leader"></span>$4</div><p>Light creamy soup with ground beef, diced shiitake mushroom, tofu, egg white and cilantro</p></div>
      </div>
    </div>
  </div>

  <div class="panel">
    <div class="frame">
      <h2>ENTRÉES</h2>
      <div class="list" style="top:70px;gap:9px">
        <span class="band">CHEF SPECIALTIES</span>
        <div class="item"><div class="row">Jasmine Tea Smoked Duck<span class="leader"></span>$24</div><p>Boneless half duck served with thinly sliced cucumber, scallion, house made duck sauce and soft flour wrap</p></div>
        <div class="item"><div class="row">Sizzling Cumin Lamb<span class="leader"></span>$16</div><p>Tender pieces of lamb rubbed in cumin, Sichuan peppers, red and green bell peppers and onions</p></div>
        <div class="item"><div class="row">Chef Liu's Spicy Beef<span class="leader"></span>$16</div><p>Angus beef in house made green peppercorn sauce with Chinese cabbage, sprouts and celery</p></div>
        <div class="item"><div class="row">Chef Liu's Spicy Fish<span class="leader"></span>$17</div><p>Fish filet in house made green peppercorn sauce with Chinese cabbage, sprouts and celery</p></div>
        <div class="item"><div class="row">General Tso's Scallops<span class="leader"></span>$18</div><p>The perfect combination of tender scallops marinated in a sweet chili sauce with broccoli and red peppers</p></div>
        <span class="band" style="margin-top:22px">BEEF &amp; PORK</span>
        <div class="item"><div class="row">Dancing Beef<span class="leader"></span>$16</div><p>Angus beef slices on a bed of sizzling rice crackers, black peppercorn and Thai chili</p></div>
        <div class="item"><div class="row">Oyster Beef<span class="leader"></span>$14</div><p>Tender cuts of steak wok fried with onions and marinated in a homemade oyster sauce</p></div>
        <div class="item"><div class="row">Double Pepper Beef<span class="leader"></span>$16</div><p>Angus steak with peppercorn, Thai chili, Serrano pepper and tofu and rice noodles</p></div>
        <div class="item"><div class="row">Black Pepper Steak<span class="leader"></span>$15</div><p>Tender cuts of steak mixed with onions and red and green bell peppers</p></div>
        <div class="item"><div class="row">Singapore Baby Back Ribs<span class="leader"></span>$16</div><p>Tender baby back ribs rubbed in a Thai inspired sweet tangy glaze</p></div>
        <div class="item"><div class="row">Dancing Pork Belly<span class="leader"></span>$15</div><p>Braised Pork Belly on sizzling rice cracker</p></div>
        <div class="item"><div class="row">Twice Cooked Pork<span class="leader"></span>$14</div><p>Stir fried Pork Belly slices with leek and fermented black beans</p></div>
      </div>
    </div>
  </div>

  <div class="panel">
    <div class="frame">
      <h2>ENTRÉES</h2>
      <div class="list" style="top:70px;gap:9px">
        <span class="band">CHICKEN</span>
        <div class="item"><div class="row">Kung Pao Chicken<span class="leader"></span>$13</div><p>Chicken sautéed with roasted peanuts and dry red chili in Kung Pao sauce</p></div>
        <div class="item"><div class="row">Orange Chicken<span class="leader"></span>$13</div><p>Battered-fried chicken breast with dried chili peppers and stir fried in a tangy orange flavored sauce</p></div>
        <div class="item"><div class="row">Double Pepper Chicken<span class="leader"></span>$15</div><p>Farm raised chicken with peppercorn, Thai chili, Serrano peppers, jalapeños, rice noodles and cilantro</p></div>
        <div class="item"><div class="row">Crispy Spicy Chicken<span class="leader"></span>$14</div><p>Crispy-diced chicken with Sichuan peppers, garlic, scallions and red and green bell peppers</p></div>
        <div class="item"><div class="row">General Tso's Chicken<span class="leader"></span>$13</div><p>Battered-fried chicken breast, stir fried in a sweet &amp; tangy chili sauce with chili peppers</p></div>
        <div class="item"><div class="row">Shredded Chicken in Spicy Garlic Sauce<span class="leader"></span>$14</div><p>Tender shredded chicken, wood ear mushrooms, bamboo shoots, broccoli and water chestnuts</p></div>
        <div class="item"><div class="row">Sweet &amp; Sour Chicken<span class="leader"></span>$13</div><p>Crispy chicken with green bell peppers, onions and pineapple glazed in a homemade sweet and sour marinade</p></div>
        <span class="band" style="margin-top:14px">SEAFOOD</span>
        <div class="item"><div class="row">Kung Pao Shrimp<span class="leader"></span>$16</div><p>Sautéed shrimp with roasted peanuts and dry red chili in Kung Pao sauce</p></div>
        <div class="item"><div class="row">Rice Wine Shrimp &amp; Tofu<span class="leader"></span>$18</div><p>Shrimp with rice wine mixed with onions, peas and carrots</p></div>
        <div class="item"><div class="row">Shrimp in Spicy Garlic Sauce<span class="leader"></span>$15</div><p>Shrimp sautéed in a spicy garlic sauce with broccoli, red and green bell peppers, bamboo shoots and mushrooms</p></div>
        <div class="item"><div class="row">Lemon Peel Shrimp<span class="leader"></span>$15</div><p>Shrimp with fresh lemons in a sweet lemon sauce on a bed of shredded lettuce</p></div>
        <div class="item"><div class="row">Rice Wine Fish<span class="leader"></span>$14</div><p>White fish filet with rice wine mixed with onions, peas and carrots</p></div>
      </div>
    </div>
  </div>

  <div class="panel">
    <div class="frame">
      <h2>NOODLES &amp; RICE</h2>
      <div class="list" style="top:56px;gap:5px">
        <div class="item"><div class="row">Lotus Bowl Fried Rice<span class="leader"></span>$12</div><p>Shrimp, chicken, and beef, farm fresh eggs, onions, and scallions</p></div>
        <div class="item"><div class="row">Vegetarian White Fried Rice<span class="leader"></span>$10</div><p>Mixed vegetables with white rice</p></div>
        <div class="item"><div class="row">Lotus Bowl Lo Mein<span class="leader"></span>$12</div><p>Shrimp, chicken, and beef, farm fresh eggs, onions, and scallions</p></div>
        <div class="item"><div class="row">Vegetarian Lo Mein<span class="leader"></span>$10</div><p>Mixed vegetables with lo mein noodles</p></div>
        <h3 class="sub" style="margin:10px 0 6px">VEGETARIAN DISHES</h3>
        <div class="item"><div class="row">Wok Tossed String Beans<span class="leader"></span>$9</div><p>Fresh string beans mixed with pickled vegetables</p></div>
        <div class="item"><div class="row">Mapo Tofu<span class="leader"></span>$11</div><p>Soft Tofu, scallion, Sichuan peppercorn and peppers</p></div>
        <div class="item"><div class="row">Spicy Garlic Eggplant<span class="leader"></span>$12</div><p>Chinese eggplant in spicy garlic sauce garnished with scallions</p></div>
        <div class="item"><div class="row">Buddha's Delight<span class="leader"></span>$10</div><p>Seasonal vegetables wok-tossed in our light soy garlic sauce</p></div>
        <div class="item"><div class="row">Stir-fried Eggplant Beans<span class="leader"></span>$12</div><p>Chinese eggplant with sautéed green beans</p></div>
        <div class="item"><div class="row">Shiitake Baby Bok-Choy<span class="leader"></span>$12</div><p>Sautéed baby bok-choy with Shiitake mushrooms in brown sauce</p></div>
        <h3 class="sub" style="margin:10px 0 6px">KIDS MENU</h3>
        <div class="item"><div class="row">Beef Lo Mein<span class="leader"></span>$5</div><p>Lo Mein noodles mixed with beef in garlic sauce</p></div>
        <div class="item"><div class="row">Chicken Fried Rice<span class="leader"></span>$5</div><p>Fried rice, farm fresh eggs, onions, and scallions</p></div>
        <div class="item"><div class="row">Sweet &amp; Sour Chicken<span class="leader"></span>$6</div><p>Bite sized crispy chicken with sweet &amp; sour sauce</p></div>
        <div class="item"><div class="row">Lemon Chicken<span class="leader"></span>$6</div><p>Bite sized crispy chicken in a sweet lemon sauce</p></div>
        <h3 class="sub" style="margin:10px 0 6px">DESSERTS</h3>
        <div class="item"><div class="row">The Great Wall of Cake<span class="leader"></span>$7</div><p>Scale this fortress of Chocolate Cake Delight</p></div>
        <div class="item"><div class="row">Cheesecake Wontons (4)<span class="leader"></span>$6</div><p>Fried wontons stuffed with cheesecake and dipped in raspberry sauce</p></div>
        <div class="item"><div class="row">Tempura Snowball<span class="leader"></span>$4</div><p>Vanilla ice cream fried in tempura batter with powdered sugar and fudge</p></div>
        <div class="item"><div class="row">Sweet Rice Patties in Caramel<span class="leader"></span>$7</div><p>Traditional Chinese dessert with sweet rice dipped in a caramel sauce</p></div>
      </div>
    </div>
  </div>
</section>

</body>
</html>
```